依頼詳細
現在、不動産業務にて空家・空地・相続させたお客様へお手紙と返信用ハガキをつけお送りしています。使用していますはがきデザインはワードで作成し、プリンターではがきに印刷しお手紙に添えてお送りしています。
返信いただくお客様に、
該当する内容に〇をつけていただき、送っていただいております。(2パターン使用中です)
お客様からの返信率はあまりない状況です。

※お客様の年齢層の幅も広いですし、相続対象者の方にもお送りしますので、お客様の中に はDMはがき自体を不快に思われる方もいらっしゃいますので、
デザインはシンプルなもので字体やバランスなどのご提案も含めお願いしたいです。
記載項目
裏面:ご回答書(ご所有の不動産について)、ご意見・ご要望、お客様のご住所・
お名前・ご連絡先
希望イメージ
シンプル 複雑
単色 カラフル
暗い 明るい
日常 高級
遊び心 厳粛
未来的 伝統的
女性的 男性的
希望する色
納品ファイル
• 高解像度JPG (.jpg)
• PNG形式 (.png)
補足説明
■ 選んだ理由

提案していただきありがとうございました。
見た瞬間から目を引かれるデザインで、柔らかい雰囲気がとても気に入りました。

■ 提案者全員のお礼・コメント

素晴らしいデザインでした!
ありがとうございました。

```html
<!DOCTYPE html>
<html lang="ja">
<head>
<meta charset="UTF-8">
<title>ご回答書</title>
<link rel="stylesheet" href="https://fonts.googleapis.com/css2?family=M+PLUS+Rounded+1c:wght@500;700&family=Noto+Sans+JP:wght@400;500;700&display=swap">
<style>
  :root {
    --sky: #a9d8f2;
    --cloud: #ffffff;
    --title: #3aa6d8;
    --ink: #222222;
    --rule: #555555;
    --grass: #8fcf6e;
    --grass-deep: #7cc15b;
    --town-top: #eef7fb;
    --town-mid: #f3e9d8;
  }
  * { margin: 0; padding: 0; box-sizing: border-box; }
  html, body { width: 811px; height: 1200px; overflow: hidden; background: #fff; }
  .card {
    position: relative; width: 811px; height: 1200px; overflow: hidden;
    font-family: "Noto Sans JP", sans-serif; color: var(--ink); background: #fff;
  }
  .sky { position: absolute; inset: 0; }
  .title {
    position: absolute; top: 88px; width: 100%; text-align: center;
    font-family: "M PLUS Rounded 1c", sans-serif; font-weight: 700;
    font-size: 44px; color: var(--title); letter-spacing: 4px;
  }
  .subtitle {
    position: absolute; top: 170px; width: 100%; text-align: center;
    font-weight: 700; font-size: 36px; letter-spacing: 1px;
  }
  .hint { position: absolute; top: 248px; left: 88px; font-size: 21px; }
  .options { position: absolute; top: 282px; left: 80px; list-style: none; }
  .options li {
    display: flex; align-items: center; height: 51px;
    font-size: 34px; font-weight: 500; letter-spacing: 1px;
  }
  .options li::before {
    content: ""; width: 28px; height: 28px; border: 2px solid var(--ink);
    margin-right: 6px; flex: none;
  }
  .contact { position: absolute; left: 70px; width: 700px; top: 645px; }
  .contact .field {
    height: 74px; border-bottom: 2px solid var(--rule);
    display: flex; align-items: flex-end; padding: 0 0 8px 4px; font-size: 24px;
  }
  .no-contact { text-align: right; font-size: 18px; margin-top: 8px; }
  .town {
    position: absolute; left: 0; top: 900px; width: 811px; height: 215px;
    background: linear-gradient(180deg, var(--town-top) 0%, var(--town-mid) 55%, var(--grass) 85%);
  }
  .thanks {
    position: absolute; left: 0; bottom: 0; width: 811px; height: 90px;
    background: var(--grass-deep); color: #fff; text-align: center;
    font-family: "M PLUS Rounded 1c", sans-serif; font-weight: 500;
    font-size: 38px; line-height: 82px; letter-spacing: 3px;
  }
</style>
</head>
<body>
<div class="card">
  <svg class="sky" width="811" height="1200" viewBox="0 0 811 1200" aria-hidden="true">
    <rect x="0" y="0" width="811" height="660" fill="var(--sky)"/>
    <path fill="var(--cloud)" d="M70 660 L70 250 C40 240 40 170 95 165 C90 110 160 85 200 115 C220 40 330 20 380 70 C420 20 520 25 545 90 C600 60 680 95 670 160 C730 160 760 220 720 255 L720 560 C760 580 770 640 760 660 Z"/>
    <rect x="0" y="640" width="811" height="560" fill="#fff"/>
    <path fill="#fff" d="M742 92 l40 -16 c8 -3 12 3 5 8 l-30 16 -2 18 -7 3 -3 -15 -14 7 -2 8 -5 2 1 -12 -10 -6 5 -2 8 4 14 -7 -12 -10 6 -2 z"/>
  </svg>

  <h1 class="title">ご回答書</h1>
  <h2 class="subtitle">ご所有の不動産について</h2>
  <p class="hint">該当に✓</p>
  <ul class="options">
    <li>売却したい</li>
    <li>売却しない</li>
    <li>売却するか迷っている</li>
    <li>不動産の価格が知りたい</li>
    <li>当分様子をみる</li>
    <li>将来自分（子供）が家を建てて住む</li>
    <li>不動産を活用したい</li>
  </ul>

  <div class="contact">
    <div class="field">ご住所：</div>
    <div class="field">お名前：</div>
    <div class="field">ご連絡先：</div>
    <p class="no-contact">□連絡を希望しない</p>
  </div>

  <div class="town" role="img" aria-label="家や木が並ぶ街並みと芝生を歩く人々のイラスト"></div>
  <p class="thanks">ご回答ありがとうございました</p>
</div>
</body>
</html>
```